Flyer for annual KESTREL SUMMIT 2020

I would like a church event flyer designed. The event is called "KESTREL SUMMIT 2020". I am looking for a professional, yet catchy design that uses our brand colors and logo creatively while communicating key information of the event effectively.

1. The logo is attached in two color formats. The designer has the choice to use them as he/she want.

2. The location of the event is: Harlow Community Center, 239 Fennimore Street, Portland, ME 04117

3. Time and date of event. The designer can organize and format the date and time as he/she pleases.
Thursday December 31st @ 6:30PM
Friday January 1st @ 6:30PM
Saturday 2nd @ 6:30PM
Sunday 3rd @ 4:30PM

4. The topic of the event is "In Fire and On Fire". The designer is free to use this phrase as he/she pleases to create a good composition.

5. Speaker: Prophet Marcus Olunde (2 pictures of the speaker to choose from are attached)

6. Contact information: contact@brightmeadowfold.org - Telephone number: 207 583 2914

7. I would also like the following three words on the flyer. These words describe the focus of the event: FIRE, REVIVAL, PROPHETIC

Target Market(s)

Young adults

Font styles to use
Sans Serif

Requirements
Must have
• Logo, speaker's picture
Should not have
• cross image, church image

```html
<!DOCTYPE html>
<html lang="en">
<head>
<meta charset="utf-8">
<title>Kestrel Summit 2020 Flyer</title>
<link rel="stylesheet" href="https://fonts.googleapis.com/css2?family=Archivo+Black&family=Merriweather:wght@400&family=Oswald:wght@600&display=swap">
<style>
  :root {
    --navy-deep: #04365a;
    --navy-glow: #17537a;
    --navy-ink: #0b3a5f;
    --orange: #f7962a;
    --white: #ffffff;
    --silver: #d3dbe3;
    --serif: "Merriweather", Georgia, serif;
    --display: "Archivo Black", "Arial Black", sans-serif;
    --condensed: "Oswald", "Arial Narrow", sans-serif;
  }
  * { box-sizing: border-box; margin: 0; padding: 0; }
  html, body { width: 849px; height: 1200px; overflow: hidden; background: var(--navy-deep); }
  .flyer {
    position: relative;
    width: 849px;
    height: 1200px;
    overflow: hidden;
    border: 1px solid #1c2833;
    background: radial-gradient(ellipse 60% 48% at 50% 55%, var(--navy-glow) 0%, #0f4669 55%, var(--navy-deep) 100%);
  }
  .brand {
    position: absolute;
    top: 92px;
    left: 0;
    width: 100%;
    text-align: center;
  }
  .brand-name {
    font-family: var(--serif);
    font-size: 56px;
    letter-spacing: 1px;
    color: var(--white);
    line-height: 1.2;
  }
  .brand-tagline {
    margin-top: 6px;
    font-family: var(--serif);
    font-size: 14px;
    letter-spacing: 0.5px;
    color: var(--orange);
  }
  .speaker-photo {
    position: absolute;
    left: 280px;
    top: 216px;
    width: 289px;
    height: 319px;
    border-radius: 50%;
    border: 7px solid var(--white);
    background: linear-gradient(180deg, #b9b2aa 0%, #8d8680 45%, #c9522f 78%, #d25a35 100%);
  }
  .speaker-name {
    position: absolute;
    top: 547px;
    width: 100%;
    text-align: center;
    font-family: var(--serif);
    font-size: 26px;
    letter-spacing: 1px;
    color: var(--silver);
  }
  .event-title {
    position: absolute;
    left: 99px;
    top: 637px;
    width: 651px;
    height: 72px;
    background: var(--white);
    border: 1px solid #2a2a2a;
    display: flex;
    align-items: center;
    justify-content: center;
    font-family: var(--display);
    font-size: 39px;
    letter-spacing: 1px;
    color: var(--navy-ink);
  }
  .schedule {
    position: absolute;
    top: 772px;
    width: 100%;
    list-style: none;
    text-align: center;
    font-family: var(--serif);
    font-size: 28px;
    letter-spacing: 1px;
    line-height: 44px;
    color: var(--white);
  }
  .venue-band {
    position: absolute;
    left: 0;
    top: 985px;
    width: 100%;
    height: 105px;
    background: var(--orange);
    display: flex;
    flex-direction: column;
    justify-content: center;
    align-items: center;
    font-family: var(--condensed);
    font-weight: 600;
    font-size: 33px;
    line-height: 40px;
    text-transform: uppercase;
    color: var(--navy-ink);
    letter-spacing: -0.5px;
  }
  .contact {
    position: absolute;
    top: 1136px;
    width: 100%;
    display: flex;
    justify-content: center;
    align-items: center;
    gap: 12px;
    font-family: var(--condensed);
    font-weight: 600;
    font-size: 25px;
    text-transform: uppercase;
    color: var(--white);
    letter-spacing: -0.3px;
  }
  .contact-divider { font-size: 25px; }
  .phone-icon { width: 12px; height: 20px; }
</style>
</head>
<body>
  <main class="flyer">
    <header class="brand">
      <div class="brand-name">VANTREL</div>
      <div class="brand-tagline">A LIGHT TO EVERY CITY</div>
    </header>

    <div class="speaker-photo" role="img" aria-label="Portrait of Prophet Marcus Olunde in an orange jacket against a brick wall"></div>
    <p class="speaker-name">Prophet Marcus Olunde</p>

    <h1 class="event-title">KESTREL SUMMIT 2020</h1>

    <ul class="schedule">
      <li>Thursday December 31st @ 6:30PM</li>
      <li>Friday January 1st @ 6:30PM</li>
      <li>Saturday 2nd @ 6:30PM</li>
      <li>Sunday 3rd @ 4:30PM</li>
    </ul>

    <section class="venue-band">
      <span>Harlow Community Center,</span>
      <span>239 Fennimore Street, Portland, ME 04117</span>
    </section>

    <footer class="contact">
      <span>contact@brightmeadowfold.org</span>
      <span class="contact-divider">|</span>
      <svg class="phone-icon" viewBox="0 0 14 22" aria-hidden="true">
        <path d="M10 2 C5 3 3 7 3 11 C3 15 5 19 10 20" fill="none" stroke="#ffffff" stroke-width="2.4" stroke-linecap="round"/>
        <rect x="8.5" y="0.5" width="4" height="5" rx="1" fill="#ffffff"/>
        <rect x="8.5" y="16.5" width="4" height="5" rx="1" fill="#ffffff"/>
      </svg>
      <span>207 583 2914</span>
    </footer>
  </main>
</body>
</html>
```